La Paloma Taberna

We need layouts for the attached 6 pages. The elements that are within the PDF are to be included in the design but their placement, the colors, everything that is there is completely up to your design ability so please get creative.
We like clean, web 2.0 type designs. Here is a restaurant with a nice design:http://tierrasolferino.example/ It does not need to be like this at all, just for a concept of what we like.
The logo on the top left of the site is our logo. I've attached it and a PDF containing the elements of the site here.

```html
<!DOCTYPE html>
<html lang="en">
<head>
<meta charset="utf-8">
<title>La Paloma Taberna — Menu</title>
<link rel="stylesheet" href="https://fonts.googleapis.com/css2?family=Cinzel:wght@400;700&family=Share+Tech+Mono&family=Lato:wght@400&family=Sorts+Mill+Goudy&display=swap">
<style>
:root{
  --wood-dark:#3a1810;
  --wood-mid:#4e2418;
  --wood-top:#6a3020;
  --gold:#d9c48f;
  --nav-text:#d6c6a8;
  --copper:#b8793a;
  --panel:#d4d2d5;
  --photo:#bdbdbd;
  --footer:rgba(70,44,36,.92);
  --reserve:#8e8886;
  --field:#c9c6c6;
  --ink:#1d1d1d;
}
*{box-sizing:border-box;margin:0;padding:0}
html,body{width:1200px;height:962px;overflow:hidden}
body{position:relative;background:var(--wood-dark);font-family:"Lato",sans-serif}
.wood{position:absolute;inset:0;background:
  repeating-linear-gradient(180deg,rgba(0,0,0,.08) 0 2px,transparent 2px 5px),
  linear-gradient(180deg,var(--wood-mid),var(--wood-dark))}
.top-band{position:absolute;left:0;top:0;width:1200px;height:52px;background:linear-gradient(180deg,var(--wood-top),#4a2014);border-bottom:2px solid #2a0e08}
.phone{position:absolute;right:100px;top:8px;font-family:"Sorts Mill Goudy",serif;font-size:29px;color:var(--gold)}
.brand{position:absolute;left:96px;top:60px;width:193px;text-align:center}
.brand-mark{width:40px;height:40px;margin:0 auto 16px;background:var(--copper)}
.brand-name{font-family:"Share Tech Mono",monospace;font-size:21px;color:#f1ead8;white-space:nowrap}
.nav-rule{position:absolute;left:298px;top:98px;width:817px;height:8px;background:#5a2a1c}
.nav{position:absolute;top:119px;left:0;list-style:none}
.nav li{position:absolute;font-family:"Share Tech Mono",monospace;font-size:29px;color:var(--nav-text);white-space:nowrap;border-bottom:1px solid #5a3326;padding-bottom:2px}
.panel{position:absolute;left:88px;top:189px;width:1023px;height:573px;background:var(--panel);border:2px solid #3a2318}
.menu-title{position:absolute;left:38px;top:38px;font-family:"Cinzel",serif;font-weight:700;font-size:34px;color:var(--copper);border-bottom:1px solid #9a8c80;padding-right:6px;line-height:1.1}
.menu-list{position:absolute;left:40px;top:120px;list-style:none}
.menu-list li{font-family:"Cinzel",serif;font-size:32px;color:var(--copper);height:62px}
.printable{position:absolute;left:44px;top:494px;font-size:16px;color:var(--copper)}
.photos{position:absolute;left:456px;top:37px;width:455px;height:474px;background:var(--photo);display:flex;align-items:center;justify-content:center;font-size:17px;color:var(--ink)}
.arrow{position:absolute;top:236px;width:56px;height:68px}
.arrow.prev{left:384px}.arrow.next{left:926px}
.footer{position:absolute;left:90px;top:765px;width:1025px;height:163px;background:var(--footer);border:1px solid #2a1710}
.reserve{position:absolute;left:34px;top:13px;width:355px;height:136px;background:var(--reserve);border-radius:6px}
.reserve h2{position:absolute;left:0;right:0;top:8px;text-align:center;font-family:"Sorts Mill Goudy",serif;font-weight:400;font-size:19px;color:#6e3f1c}
.field{position:absolute;height:32px;background:var(--field);border:1px solid #b88d5a;font-family:"Sorts Mill Goudy",serif;font-size:20px;color:var(--ink);display:flex;align-items:center;justify-content:space-between;padding:0 4px 0 8px}
.icon{position:absolute}
.find{position:absolute;left:199px;top:86px;width:149px;height:36px;background:var(--copper);border:1px solid #6b4424;border-radius:5px;font-family:"Sorts Mill Goudy",serif;font-size:20px;color:var(--ink);display:flex;align-items:center;justify-content:center}
.links{position:absolute;left:454px;top:22px}
.links h3{font-family:"Sorts Mill Goudy",serif;font-weight:400;font-size:26px;color:#111}
.links span{display:block;width:239px;border-bottom:1px solid #111;height:37px}
.social{position:absolute;left:799px;top:99px;display:flex;gap:38px}
.social div{width:37px;text-align:center;font-size:10px;color:#e8dccb}
.social i{display:block;width:37px;height:37px;background:#8a6a55;margin-bottom:2px}
</style>
</head>
<body>
<div class="wood" role="img" aria-label="Dark stained wood plank background"></div>
<div class="top-band"></div>
<div class="phone">Phone : 709 555 0142</div>

<header class="brand">
  <div class="brand-mark"></div>
  <div class="brand-name">La Paloma Taberna</div>
</header>

<div class="nav-rule"></div>
<ul class="nav">
  <li style="left:310px">HOME</li>
  <li style="left:411px">MENU</li>
  <li style="left:515px">CONTACT</li>
  <li style="left:675px">CALENDAR</li>
  <li style="left:856px">PRESS</li>
  <li style="left:984px">GALLERY</li>
</ul>

<main class="panel">
  <h1 class="menu-title">MENU</h1>
  <ul class="menu-list">
    <li>LUNCH</li><li>DINNER</li><li>TEQUILAS</li><li>WINELIST</li><li>CHAMPAGNE</li>
  </ul>
  <div class="printable">PRINTABLE MENU</div>
  <svg class="arrow prev" viewBox="0 0 56 68"><path d="M40 4 L6 34 L40 64 L52 56 L26 34 L52 12 Z" fill="#e87424" stroke="#b8561a" stroke-width="2"/></svg>
  <div class="photos">MENU PHOTOS</div>
  <svg class="arrow next" viewBox="0 0 56 68"><path d="M16 4 L50 34 L16 64 L4 56 L30 34 L4 12 Z" fill="#e87424" stroke="#b8561a" stroke-width="2"/></svg>
</main>

<footer class="footer">
  <section class="reserve">
    <h2>Make a Reservation</h2>
    <svg class="icon" style="left:8px;top:46px" width="30" height="30" viewBox="0 0 30 30"><rect x="1" y="1" width="28" height="28" fill="#fff" stroke="#333"/><path d="M1 15H29M15 1V15" stroke="#333"/></svg>
    <div class="field" style="left:53px;top:44px;width:146px">06/19/2014<span>&#8964;</span></div>
    <svg class="icon" style="left:204px;top:44px" width="32" height="32" viewBox="0 0 32 32"><circle cx="16" cy="16" r="14" fill="#fff" stroke="#333" stroke-width="2"/><path d="M16 16 L10 26" stroke="#333" stroke-width="2"/></svg>
    <div class="field" style="left:241px;top:44px;width:103px">7:00 pm<span>&#8964;</span></div>
    <svg class="icon" style="left:8px;top:86px" width="36" height="36" viewBox="0 0 36 36"><rect x="1" y="1" width="34" height="34" fill="#fff" stroke="#333"/><circle cx="18" cy="13" r="6" fill="none" stroke="#333" stroke-width="1.5"/><path d="M7 33 C8 23 28 23 29 33" fill="none" stroke="#333" stroke-width="1.5"/></svg>
    <div class="field" style="left:53px;top:86px;width:116px">3 People<span>&#8964;</span></div>
    <div class="find">Find a Table</div>
  </section>
  <nav class="links">
    <h3>Links</h3>
    <span></span><span></span>
  </nav>
  <div class="social">
    <div><i></i>Chirrup</div>
    <div><i></i>Amigos</div>
    <div><i></i>Fotito</div>
  </div>
</footer>
</body>
</html>
```